50% off blue price stickers - poster

I am looking for a poster to hang in our retail discount store that let's people know they take 50% off the marked price on anything with a blue price sticker. We try and tell them as they walk in but can't catch everyone. If they don't know, they don't see the value in the pricing. We mark the retail price with a blue price tag and they get 50% off that price. We sell items from wholesale clubs (Brindle, JETs Depot) and offer 50% off what they sell the items for. Clothes, Housewares, Kitchenware, Furniture, Bath and Body, Electronics, Jewelry - you name it.
Updates

Check out our Chirpbook page - Marla's Found Again, in Brentwood, California to learn more about us and our merchandise.

For poster size - we are looking at 20" wide by 30" long. Thank you.

Target Market(s)

Ages 35-50

Industry/Entity Type

Retail

Font styles to use
Serif

Requirements
Must have
• Store name - Marla's Found Again
Nice to have
• Not too cluttered - easy to read to get the point across quickly. Something that incorporates our logo - but doesn't have to stick with the red/black theme, especially if you are using blue themes in the poster. Maybe just use the theme of the logo so the fonts are similar....

```html
<!DOCTYPE html>
<html lang="en">
<head>
<meta charset="utf-8">
<title>50% Off Blue Stickers – Marla's Found Again</title>
<link href="https://fonts.googleapis.com/css2?family=Poppins:wght@500;600&family=Kaushan+Script&display=swap" rel="stylesheet">
<style>
  :root {
    --paper: #ffffff;
    --sticker-blue: #0a2a9c;
    --flap-light: #1a8cff;
    --flap-mid: #0b63e0;
    --fold-shade: #061b6b;
    --sticker-shadow: #d2d2d2;
    --headline-red: #e0141b;
    --text-blue: #0a2a9c;
    --white: #ffffff;
    --brand-green: #0f4d3a;
  }
  html, body {
    margin: 0;
    padding: 0;
    overflow: hidden;
    background: var(--paper);
  }
  .poster {
    position: relative;
    width: 800px;
    height: 1200px;
    background: var(--paper);
    overflow: hidden;
    font-family: "Poppins", "Century Gothic", sans-serif;
  }
  .sticker-art {
    position: absolute;
    inset: 0;
    width: 800px;
    height: 1200px;
  }
  .line {
    position: absolute;
    left: 22px;
    width: 778px;
    margin: 0;
    text-align: center;
    line-height: 1;
    white-space: nowrap;
  }
  .discount-value {
    top: 210px;
    font-size: 170px;
    font-weight: 600;
    color: var(--white);
    letter-spacing: 2px;
  }
  .discount-label {
    top: 392px;
    font-size: 95px;
    font-weight: 600;
    color: var(--white);
    letter-spacing: 2px;
  }
  .headline-anything {
    top: 592px;
    font-size: 92px;
    font-weight: 600;
    color: var(--headline-red);
  }
  .connector-word {
    position: absolute;
    left: 377px;
    top: 651px;
    width: 72px;
    height: 72px;
    border-radius: 50%;
    background: var(--text-blue);
    color: var(--white);
    font-family: "Kaushan Script", cursive;
    font-size: 22px;
    line-height: 72px;
    text-align: center;
  }
  .headline-blue {
    top: 694px;
    font-size: 155px;
    font-weight: 500;
    color: var(--text-blue);
    letter-spacing: 6px;
  }
  .headline-stickers {
    top: 808px;
    font-size: 105px;
    font-weight: 600;
    color: var(--text-blue);
  }
  .underline-bar {
    position: absolute;
    left: 184px;
    top: 931px;
    width: 455px;
    height: 17px;
    background: var(--text-blue);
  }
  .store-mark {
    position: absolute;
    left: 22px;
    width: 778px;
    top: 1004px;
    display: flex;
    justify-content: center;
    align-items: center;
    gap: 10px;
  }
  .store-mark-dot {
    width: 40px;
    height: 40px;
    border-radius: 50%;
    background: var(--brand-green);
  }
  .store-mark-name {
    font-size: 24px;
    font-weight: 600;
    color: var(--headline-red);
  }
</style>
</head>
<body>
<main class="poster">
  <svg class="sticker-art" viewBox="0 0 800 1200" aria-hidden="true">
    <defs>
      <linearGradient id="flapGradient" x1="0" y1="0" x2="1" y2="1">
        <stop offset="0" stop-color="var(--flap-light)"/>
        <stop offset="1" stop-color="var(--flap-mid)"/>
      </linearGradient>
    </defs>
    <circle class="sticker-shadow" cx="411" cy="330" r="232" fill="var(--sticker-shadow)"/>
    <circle class="sticker-body" cx="411" cy="318" r="232" fill="var(--sticker-blue)"/>
    <path class="sticker-fold-shade" d="M297 109 Q470 262 636 192 Q470 236 297 109 Z" fill="var(--fold-shade)"/>
    <path class="sticker-flap" d="M297 109 L636 192 Q470 236 297 109 Z" fill="url(#flapGradient)"/>
    <rect class="discount-rule" x="240" y="375" width="358" height="7" fill="var(--white)"/>
  </svg>

  <p class="line discount-value">50%</p>
  <p class="line discount-label">OFF</p>

  <h1 class="line headline-anything">anything</h1>
  <span class="connector-word">with</span>
  <p class="line headline-blue">BLUE</p>
  <p class="line headline-stickers">stickers</p>
  <div class="underline-bar"></div>

  <div class="store-mark">
    <span class="store-mark-dot"></span>
    <span class="store-mark-name">Marla's Found Again</span>
  </div>
</main>
</body>
</html>
```